Gravaloop bottle design

We're a small company looking for someone to help with our bottle design. We provide a sauce that will boost the flavor of packaged ramen. We're looking for a label that will stand out. I'm attaching some of the labels we like and some that I've made.

```html
<!DOCTYPE html>
<html lang="en">
<head>
<meta charset="utf-8">
<title>Gravaloop Ramen Sauce Label</title>
<link rel="stylesheet" href="https://fonts.googleapis.com/css2?family=Zen+Dots&family=Orbitron:wght@600&display=swap">
<style>
  :root {
    --page-bg: #ece9e4;
    --label-red: #c41e24;
    --label-red-deep: #a8161c;
    --ink: #111111;
    --white: #ffffff;
    --burst-yellow: #f2d43a;
    --burst-red: #e5262b;
    --ornament: #8e1418;
  }
  html, body {
    margin: 0;
    padding: 0;
    width: 1200px;
    height: 1200px;
    overflow: hidden;
    background: var(--page-bg);
  }
  .canvas {
    position: relative;
    width: 1200px;
    height: 1200px;
  }
  .label {
    position: absolute;
    left: 414px;
    top: 40px;
    width: 372px;
    height: 1120px;
    box-shadow: 0 10px 30px rgba(0,0,0,0.18);
  }
  .label svg { display: block; }
  .brand-name {
    font-family: "Orbitron", sans-serif;
    font-weight: 600;
    fill: var(--white);
    letter-spacing: 2px;
  }
  .product-name {
    font-family: "Zen Dots", sans-serif;
    fill: var(--ink);
    letter-spacing: 1px;
  }
  .volume {
    font-family: "Orbitron", sans-serif;
    font-weight: 600;
    fill: var(--ink);
  }
</style>
</head>
<body>
<main class="canvas">
  <div class="label">
    <svg width="372" height="1120" viewBox="0 0 372 1120">
      <defs>
        <linearGradient id="label-red-fill" x1="0" y1="0" x2="1" y2="1">
          <stop offset="0" stop-color="var(--label-red-deep)"/>
          <stop offset="0.5" stop-color="var(--label-red)"/>
          <stop offset="1" stop-color="var(--label-red-deep)"/>
        </linearGradient>
      </defs>

      <!-- label body -->
      <rect class="label-body" x="0" y="0" width="372" height="1120" fill="url(#label-red-fill)"/>

      <!-- top band -->
      <rect class="top-band" x="0" y="0" width="372" height="12" fill="var(--ink)"/>
      <rect class="top-rule" x="0" y="18" width="372" height="3" fill="var(--ink)"/>

      <!-- bottom band -->
      <rect class="bottom-rule" x="0" y="1072" width="372" height="3" fill="var(--ink)"/>
      <rect class="bottom-band" x="0" y="1082" width="372" height="38" fill="var(--ink)"/>

      <!-- corner ornaments -->
      <rect class="ornament-branch" x="10" y="38" width="66" height="90" rx="8" fill="var(--ornament)" opacity="0.45" role="img" aria-label="Ink drawing of a blossom branch"/>
      <rect class="ornament-crane" x="294" y="56" width="58" height="70" rx="8" fill="var(--ornament)" opacity="0.45" role="img" aria-label="Ink drawing of a flying crane"/>
      <rect class="ornament-mountains" x="8" y="860" width="96" height="166" rx="8" fill="var(--ornament)" opacity="0.45" role="img" aria-label="Ink drawing of misty mountains"/>
      <rect class="ornament-crane-low" x="104" y="885" width="64" height="64" rx="8" fill="var(--ornament)" opacity="0.45" role="img" aria-label="Ink drawing of a crane in flight"/>

      <!-- brand -->
      <circle class="brand-dot" cx="186" cy="109" r="56" fill="var(--white)"/>
      <text class="brand-name" x="186" y="186" font-size="20" text-anchor="middle">GRAVALOOP</text>

      <!-- mascot illustration area -->
      <rect class="mascot" x="38" y="269" width="256" height="366" rx="20" fill="#e8e3de" role="img" aria-label="Illustration of a cartoon panda eating ramen noodles with chopsticks"/>

      <!-- product name -->
      <text class="product-name" x="186" y="728" font-size="66" text-anchor="middle">RAMEN</text>
      <text class="product-name" x="186" y="830" font-size="66" text-anchor="middle">SAUCE</text>

      <!-- volume burst -->
      <polygon class="volume-burst"
        points="294,870 306,905 335,880 330,917 370,910 342,938 372,955 338,968 360,1000 322,995 318,1030 296,1005 272,1032 266,996 230,1004 250,972 216,958 248,940 224,908 262,916 258,880 282,904"
        fill="var(--burst-red)" stroke="var(--burst-yellow)" stroke-width="5" stroke-linejoin="round"/>
      <text class="volume" x="294" y="962" font-size="26" text-anchor="middle">8 OZ</text>
    </svg>
  </div>
</main>
</body>
</html>
```